Cybersecurity Start-Up - Korvelo

We need a power-point design for a new company based in Madrid (Spain) called 'Korvelo'. We aim to provide cybersecurity services to small- medium size companies for whom security is critical but paying big money to huge companies is not affordable.

The final design should communicate several things. As technology company which provides cybersecurity, it should be seen as something modern and futuristic , combined with safety and protection.

The company name Korvelo comes from Numantia, an ancient Celtiberian settlement in Spain which is famous for its role in the Celtiberian Wars (130 BC). They fought with Rome for 20 years , while being numerical inferior. And they won several times. When a final siege ocurred after a massive deployment of Rome legions, they held their ground for more than a year without food. When the situation was not longer sustainable, they decided to commit suicide rather than become slaves.

So the vision to hold the ground no matter what, should be communicated too
Updates

Need extra days to review

Requirements
Must have
• Check files attached for the logo of the company

```html
<!DOCTYPE html>
<html lang="en">
<head>
<meta charset="utf-8">
<title>Korvelo – Presentation Template</title>
<link href="https://fonts.googleapis.com/css2?family=Montserrat:wght@400;600;700&family=Open+Sans:wght@400;600;700&display=swap" rel="stylesheet">
<style>
:root{
  --orange:#f26522;
  --orange-light:#f7941d;
  --orange-pale:#fde3d3;
  --dark:#1d1d1f;
  --panel:#26272b;
  --ink:#2b2b2b;
  --grey:#8d8d8d;
  --grey-light:#c9c9c9;
  --canvas:#e6e6e6;
  --white:#ffffff;
}
*{margin:0;padding:0;box-sizing:border-box}
html,body{width:1200px;height:1002px;overflow:hidden;background:var(--canvas)}
body{position:relative;font-family:"Open Sans",sans-serif;color:var(--ink)}
.slide{position:absolute;width:280px;height:158px;background:var(--white);overflow:hidden}
.abs{position:absolute}
.c1{left:15px}.c2{left:311px}.c3{left:608px}.c4{left:903px}
.r1{top:38px}.r2{top:232px}.r3{top:424px}.r4{top:616px}.r5{top:809px}

.stripes{position:absolute;inset:0;width:280px;height:158px}
.title-big{position:absolute;font-family:"Montserrat",sans-serif;font-weight:400;font-size:10px;letter-spacing:1.1px;color:var(--orange)}
.subtitle{position:absolute;font-size:3.4px;color:var(--orange)}
.brand{position:absolute;font-family:"Montserrat",sans-serif;font-weight:600;font-size:15px;color:var(--ink);line-height:1}
.brand-tag{position:absolute;font-family:"Montserrat",sans-serif;font-size:2.8px;letter-spacing:1.6px;color:var(--ink)}
.photo-circle{position:absolute;border-radius:50%;border:4px solid #eef0f2;box-shadow:0 0 6px rgba(0,0,0,.25)}

.head-bar{position:absolute;left:0;top:8px;width:2px;height:8px;background:var(--orange)}
.head-title{position:absolute;left:12px;top:8px;font-size:5.6px;color:var(--orange)}
.head-rule{position:absolute;left:12px;right:12px;top:17px;height:.5px;background:var(--orange-light)}
.head-logo{position:absolute;right:13px;top:9.5px;font-family:"Montserrat",sans-serif;font-weight:600;font-size:3.6px;color:var(--ink)}
.url{position:absolute;left:12px;bottom:5px;font-size:2.6px;color:var(--ink)}
.pg{position:absolute;right:12px;bottom:3px;width:6px;height:6px;background:var(--orange);color:var(--white);font-size:2.6px;text-align:center;line-height:6px}

.txt{position:absolute;font-size:3px;line-height:4px;color:var(--grey)}
.txt.w{color:#d8d8d8}
.label{position:absolute;font-size:3.4px;color:var(--ink);font-weight:600}
.pill{position:absolute;height:6px;border-radius:3px;border:.6px solid var(--orange);font-size:3px;line-height:5px;padding:0 5px;color:var(--ink);background:var(--white)}
.pill.fill{background:var(--orange-light);border-color:var(--orange-light)}
.panel{position:absolute;background:linear-gradient(160deg,#303136,#18191c)}
.dot{position:absolute;width:3px;height:3px;border-radius:50%}
.sq{position:absolute;width:4px;height:4px;background:var(--orange-light)}
.member{position:absolute;width:40px;text-align:center;font-size:3px;line-height:4px;color:var(--grey)}
.member b{color:var(--ink);font-weight:600}
</style>
</head>
<body>

<!-- 1 Title light -->
<section class="slide c1 r1">
  <svg class="stripes" viewBox="0 0 280 158"><polygon points="256,0 268,0 238,50 226,50" fill="var(--orange)"/><polygon points="272,0 280,0 280,6 252,50 244,50" fill="var(--orange-light)"/><polygon points="216,134 228,134 214,158 202,158" fill="var(--orange)"/><polygon points="232,134 244,134 230,158 218,158" fill="var(--orange-light)"/></svg>
  <div class="title-big" style="left:24px;top:33px">PRESENTATION TITLE HERE</div>
  <div class="subtitle" style="left:24px;top:50px">Your Subtitle Goes Here</div>
  <div class="brand" style="left:24px;top:104px">Korvelo</div>
  <div class="brand-tag" style="left:25px;top:121px">CYBERSECURITY</div>
  <div class="photo-circle" role="img" aria-label="Photo of business people reviewing documents" style="left:172px;top:37px;width:91px;height:91px;background:radial-gradient(circle at 40% 40%,#f4f6f8,#aab6c2)"></div>
</section>

<!-- 2 Title dark -->
<section class="slide c2 r1">
  <div class="abs" style="left:0;top:0;width:280px;height:115px;background:#000"></div>
  <svg class="stripes" viewBox="0 0 280 158"><polygon points="256,0 268,0 238,50 226,50" fill="var(--orange)"/><polygon points="272,0 280,0 280,6 252,50 244,50" fill="var(--orange-light)"/><polygon points="216,134 228,134 214,158 202,158" fill="var(--orange)"/><polygon points="232,134 244,134 230,158 218,158" fill="var(--orange-light)"/></svg>
  <div class="title-big" style="left:24px;top:26px">PRESENTATION TITLE HERE</div>
  <div class="subtitle" style="left:24px;top:42px">Your Subtitle Goes Here</div>
  <div class="brand" style="left:24px;top:127px">Korvelo</div>
  <div class="brand-tag" style="left:25px;top:143px">CYBERSECURITY</div>
  <div class="photo-circle" role="img" aria-label="Photo of a hand signing a document" style="left:172px;top:34px;width:92px;height:92px;background:radial-gradient(circle at 45% 45%,#fafbfc,#9fb0c0)"></div>
</section>

<!-- 3 Table of contents -->
<section class="slide c3 r1">
  <div class="head-bar"></div><div class="head-title">Table of Contents</div><div class="head-rule"></div><div class="head-logo">Korvelo</div>
  <div class="label" style="left:29px;top:48px">01</div><div class="txt" style="left:46px;top:48px;color:var(--ink)">Lorem ipsum dolor</div>
  <div class="label" style="left:110px;top:48px">02</div><div class="txt" style="left:127px;top:48px;color:var(--ink)">Lorem ipsum dolor</div>
  <div class="label" style="left:191px;top:48px">03</div><div class="txt" style="left:208px;top:48px;color:var(--ink)">Lorem ipsum dolor</div>
  <div class="label" style="left:29px;top:79px">04</div><div class="txt" style="left:46px;top:79px;color:var(--ink)">Lorem ipsum dolor</div>
  <div class="label" style="left:110px;top:79px">05</div><div class="txt" style="left:127px;top:79px;color:var(--ink)">Lorem ipsum dolor</div>
  <div class="label" style="left:191px;top:79px">06</div><div class="txt" style="left:208px;top:79px;color:var(--ink)">Lorem ipsum dolor</div>
  <div class="label" style="left:29px;top:111px">07</div><div class="txt" style="left:46px;top:111px;color:var(--ink)">Lorem ipsum dolor</div>
  <div class="label" style="left:110px;top:111px">08</div><div class="txt" style="left:127px;top:111px;color:var(--ink)">Lorem ipsum dolor</div>
  <div class="label" style="left:191px;top:111px">09</div><div class="txt" style="left:208px;top:111px;color:var(--ink)">Lorem ipsum dolor</div>
  <div class="url">www.korvelo.com</div><div class="pg">01</div>
</section>

<!-- 4 Executive summary -->
<section class="slide c4 r1">
  <div class="head-bar"></div><div class="head-title">Executive Summary</div><div class="head-rule"></div><div class="head-logo">Korvelo</div>
  <div class="abs" role="img" aria-label="Photo of city towers with a hand writing" style="left:13px;top:20px;width:59px;height:128px;background:linear-gradient(180deg,#dfe8f1,#8aa2bb)"></div>
  <div class="sq" style="left:70px;top:30px"></div><div class="txt" style="left:82px;top:29px;width:185px">Protection for growing firms, built to hold the line every single day.</div>
  <div class="sq" style="left:70px;top:55px"></div><div class="txt" style="left:82px;top:54px;width:185px">Threat monitoring around the clock with clear reports and fast response.</div>
  <div class="sq" style="left:70px;top:80px"></div><div class="txt" style="left:82px;top:79px;width:185px">Affordable plans for small and medium teams across Spain and Europe.</div>
  <div class="sq" style="left:70px;top:105px"></div><div class="txt" style="left:82px;top:104px;width:185px">Audits, training and recovery planning delivered by one trusted partner.</div>
  <div class="sq" style="left:70px;top:130px"></div><div class="txt" style="left:82px;top:129px;width:185px">Modern tools, steady people and a promise never to give ground.</div>
  <div class="url">www.korvelo.com</div><div class="pg">02</div>
</section>

<!-- 5 Section dark photo -->
<section class="slide c1 r2">
  <div class="abs" role="img" aria-label="Photo of an office with screens, darkened" style="inset:0;background:linear-gradient(90deg,#1a1a1a 0%,#2e2e30 45%,#8a8a8a 80%,#c8c8c8 100%)"></div>
  <div class="head-logo" style="color:var(--white)">Korvelo</div>
  <div class="abs" style="left:102px;top:33px;font-size:5.6px;color:var(--orange)">Lorem Ipsum Dolor Sit Amet</div>
  <svg class="abs" style="left:120px;top:48px" width="50" height="60" viewBox="0 0 50 60">
    <circle cx="25" cy="22" r="15" fill="none" stroke="#fff" stroke-width="3"/><circle cx="25" cy="22" r="8" fill="none" stroke="#fff" stroke-width="3"/><circle cx="25" cy="22" r="2.5" fill="#fff"/>
    <line x1="25" y1="22" x2="42" y2="6" stroke="#fff" stroke-width="2"/>
    <line x1="15" y1="33" x2="8" y2="46" stroke="#fff" stroke-width="1"/><line x1="35" y1="33" x2="42" y2="46" stroke="#fff" stroke-width="1"/>
    <circle cx="8" cy="50" r="5" fill="var(--orange-light)"/><circle cx="42" cy="50" r="5" fill="var(--orange-light)"/>
  </svg>
  <div class="txt w" style="left:30px;top:88px;width:88px;text-align:justify">We guard networks for small firms, spot threats early and keep vital data safe from harm each day.</div>
  <div class="txt w" style="left:181px;top:88px;width:88px;text-align:justify">Our team holds the line with steady care, clear reports and quick action whenever risk appears.</div>
  <div class="url" style="color:#ddd">www.korvelo.com</div><div class="pg">03</div>
</section>

<!-- 6 Dark panel grid -->
<section class="slide c2 r2">
  <div class="head-bar"></div><div class="head-title">Title Goes Here</div><div class="head-rule"></div><div class="head-logo">Korvelo</div>
  <div class="panel" style="left:13px;top:25px;width:255px;height:119px"></div>
  <div class="txt w" style="left:29px;top:36px;width:68px">Threat scans run daily across every device and cloud account.</div>
  <div class="txt w" style="left:111px;top:36px;width:68px">Firewalls are tuned to block hostile traffic before it lands.</div>
  <div class="txt w" style="left:193px;top:36px;width:68px">Backups are tested so recovery is quick after any incident.</div>
  <div class="txt w" style="left:29px;top:71px;width:68px">Staff learn to spot phishing and weak passwords early.</div>
  <div class="txt w" style="left:111px;top:71px;width:68px">Access rules keep sensitive files with the right people only.</div>
  <div class="txt w" style="left:193px;top:71px;width:68px">Alerts reach our analysts within minutes, day or night.</div>
  <div class="txt w" style="left:29px;top:106px;width:68px">Reports show clear trends and progress for your board.</div>
  <div class="txt w" style="left:111px;top:106px;width:68px">Audits check compliance against current European rules.</div>
  <div class="txt w" style="left:193px;top:106px;width:68px">Plans grow with your team without surprise costs.</div>
  <div class="dot" style="left:21px;top:37px;background:#ccc"></div><div class="dot" style="left:103px;top:37px;background:#ccc"></div><div class="dot" style="left:185px;top:37px;background:#ccc"></div>
  <div class="dot" style="left:21px;top:72px;background:#ccc"></div><div class="dot" style="left:103px;top:72px;background:#ccc"></div><div class="dot" style="left:185px;top:72px;background:#ccc"></div>
  <div class="dot" style="left:21px;top:107px;background:#ccc"></div><div class="dot" style="left:103px;top:107px;background:#ccc"></div><div class="dot" style="left:185px;top:107px;background:#ccc"></div>
  <div class="url">www.korvelo.com</div><div class="pg">04</div>
</section>

<!-- 7 Panel left, list right -->
<section class="slide c3 r2">
  <div class="head-bar"></div><div class="head-title">Title Goes Here</div><div class="head-rule"></div><div class="head-logo">Korvelo</div>
  <div class="panel" style="left:13px;top:26px;width:122px;height:122px"></div>
  <div class="pill fill" style="left:20px;top:35px">Lorem Ipsum</div>
  <div class="txt w" style="left:28px;top:46px;width:100px">Round the clock watch on every network.<br>Rapid response when alerts are raised.</div>
  <div class="pill fill" style="left:20px;top:85px">Lorem Ipsum Dolor Sit Amet</div>
  <div class="txt w" style="left:28px;top:96px;width:100px">Clear reports for managers each month.<br>Training that keeps teams alert.<br>Recovery plans tested every quarter.</div>
  <div class="pill" style="left:156px;top:36px">Lorem Ipsum Dolo Sit Amet</div>
  <div class="txt" style="left:164px;top:50px;width:100px">Secure email and shared files for all staff.<br><br>Patch updates applied within one day.<br><br>Device checks for remote workers.<br><br>Encrypted backups stored in Spain.</div>
  <div class="url">www.korvelo.com</div><div class="pg">05</div>
</section>

<!-- 8 Steps -->
<section class="slide c4 r2">
  <div class="head-bar"></div><div class="head-title">Title Goes Here</div><div class="head-rule"></div><div class="head-logo">Korvelo</div>
  <div class="txt" style="left:40px;top:25px;width:200px;text-align:center">A clear path from first audit to full protection, step by step.</div>
  <div class="pill" style="left:18px;top:57px">Lorem Ipsum Dolo Sit Amet</div>
  <div class="pill" style="left:150px;top:57px">Lorem Ipsum Dolo Sit Amet</div>
  <div class="txt" style="left:23px;top:74px;width:110px;line-height:11px"><b style="color:var(--ink)">Step 1 :</b> Map every asset<br><b style="color:var(--ink)">Step 2 :</b> Find weak points<br><b style="color:var(--ink)">Step 3 :</b> Close the gaps</div>
  <div class="txt" style="left:155px;top:74px;width:110px;line-height:11px"><b style="color:var(--ink)">Step 4 :</b> Train the team<br><b style="color:var(--ink)">Step 5 :</b> Watch all traffic<br><b style="color:var(--ink)">Step 6 :</b> Respond quickly<br><b style="color:var(--ink)">Step 7 :</b> Review and improve</div>
  <div class="url">www.korvelo.com</div><div class="pg">06</div>
</section>

<!-- 9 Band and bubble -->
<section class="slide c1 r3">
  <div class="head-bar"></div><div class="head-title">Title Goes Here</div><div class="head-rule"></div><div class="head-logo">Korvelo</div>
  <div class="panel" style="left:14px;top:23px;width:255px;height:72px"></div>
  <div class="pill fill" style="left:117px;top:26px">Lorem Ipsum</div>
  <div class="txt w" style="left:28px;top:48px;width:70px">Security checks sized for small teams and tight budgets.</div>
  <div class="txt w" style="left:110px;top:48px;width:70px">Live monitoring with named experts who know your systems.</div>
  <div class="txt w" style="left:191px;top:48px;width:70px">Rapid recovery so work resumes within hours, not days.</div>
  <svg class="abs" style="left:11px;top:100px" width="50" height="46" viewBox="0 0 50 46"><path d="M25 4 a20 17 0 1 0 14 32 l8 6 -3-10 a20 17 0 0 0 -19-28z" fill="#fff" stroke="var(--orange-pale)" stroke-width="3"/></svg>
  <div class="txt" style="left:22px;top:119px;color:var(--ink)">Lorem Ipsum</div>
  <div class="txt" style="left:86px;top:105px;width:180px">Staff receive short monthly lessons on safe habits online.</div>
  <div class="txt" style="left:92px;top:119px;width:175px">Every login is checked against known breach lists.</div>
  <div class="txt" style="left:98px;top:133px;width:170px">Devices are scanned and patched without slowing work.</div>
  <div class="url">www.korvelo.com</div><div class="pg">07</div>
</section>

<!-- 10 Hexagons -->
<section class="slide c2 r3">
  <div class="head-bar"></div><div class="head-title">Title Goes Here</div><div class="head-rule"></div><div class="head-logo">Korvelo</div>
  <svg class="abs" style="left:40px;top:38px" width="80" height="100" viewBox="0 0 80 100">
    <g stroke="#fff" stroke-width="1">
      <polygon points="20,4 33,11 33,26 20,33 7,26 7,11" fill="#f2f2f2"/>
      <polygon points="46,4 59,11 59,26 46,33 33,26 33,11" fill="var(--orange-light)"/>
      <polygon points="33,27 46,34 46,49 33,56 20,49 20,34" fill="#8a8a8a"/>
      <polygon points="59,27 72,34 72,49 59,56 46,49 46,34" fill="#f2f2f2"/>
      <polygon points="20,50 33,57 33,72 20,79 7,72 7,57" fill="#f2f2f2"/>
      <polygon points="46,50 59,57 59,72 46,79 33,72 33,57" fill="var(--orange)"/>
    </g>
    <circle cx="19" cy="17" r="3" fill="none" stroke="var(--orange)"/><circle cx="59" cy="41" r="3" fill="none" stroke="#999"/><circle cx="20" cy="63" r="3" fill="none" stroke="var(--orange)"/>
    <text x="46" y="20" font-size="3" fill="#fff" text-anchor="middle">Lorem</text><text x="33" y="43" font-size="3" fill="#fff" text-anchor="middle">Lorem</text><text x="46" y="66" font-size="3" fill="#fff" text-anchor="middle">Lorem</text>
  </svg>
  <svg class="abs" style="left:135px;top:40px" width="12" height="92" viewBox="0 0 12 92"><circle cx="6" cy="6" r="5" fill="none" stroke="var(--orange)" stroke-width=".8"/><circle cx="6" cy="45" r="5" fill="none" stroke="var(--orange)" stroke-width=".8"/><circle cx="6" cy="84" r="5" fill="none" stroke="var(--orange)" stroke-width=".8"/></svg>
  <div class="label" style="left:155px;top:41px">Lorem Ipsum Dolor</div><div class="txt" style="left:155px;top:47px;width:110px">Quick audits reveal hidden risks in your network setup.</div>
  <div class="label" style="left:155px;top:80px">Lorem Ipsum Dolor</div><div class="txt" style="left:155px;top:86px;width:110px">Managed defence keeps attackers out around the clock.</div>
  <div class="label" style="left:155px;top:119px">Lorem Ipsum Dolor</div><div class="txt" style="left:155px;top:125px;width:110px">Bright ideas and fresh tools keep you one step ahead.</div>
  <div class="url">www.korvelo.com</div><div class="pg">08</div>
</section>

<!-- 11 Timeline -->
<section class="slide c3 r3">
  <div class="head-bar"></div><div class="head-title">Title Goes Here</div><div class="head-rule"></div><div class="head-logo">Korvelo</div>
  <div class="abs" style="left:34px;top:69px;width:42px;height:9px;background:var(--orange);color:#fff;font-size:5px;text-align:center;line-height:9px">2001</div>
  <div class="abs" style="left:76px;top:78px;width:42px;height:9px;background:#9b9b9b;color:#fff;font-size:5px;text-align:center;line-height:9px">2005</div>
  <div class="abs" style="left:118px;top:69px;width:42px;height:9px;background:var(--orange-light);color:#fff;font-size:5px;text-align:center;line-height:9px">2010</div>
  <div class="abs" style="left:160px;top:78px;width:42px;height:9px;background:#9b9b9b;color:#fff;font-size:5px;text-align:center;line-height:9px">2015</div>
  <div class="abs" style="left:202px;top:69px;width:42px;height:9px;background:var(--orange);color:#fff;font-size:5px;text-align:center;line-height:9px">2020</div>
  <div class="label" style="left:74px;top:37px;font-size:3px">Heading Goes Here</div><div class="txt" style="left:70px;top:43px;width:50px;text-align:center">First office opened with a small team.</div>
  <div class="label" style="left:158px;top:38px;font-size:3px">Heading Goes Here</div><div class="txt" style="left:154px;top:44px;width:50px;text-align:center">Regional growth and new clients.</div>
  <div class="label" style="left:34px;top:93px;font-size:3px">Heading Goes Here</div><div class="txt" style="left:30px;top:99px;width:50px;text-align:center">Early research into network defence.</div>
  <div class="label" style="left:118px;top:93px;font-size:3px">Heading Goes Here</div><div class="txt" style="left:114px;top:99px;width:50px;text-align:center">Launch of managed security plans.</div>
  <div class="label" style="left:203px;top:93px;font-size:3px">Heading Goes Here</div><div class="txt" style="left:199px;top:99px;width:50px;text-align:center">Full coverage across Spain.</div>
  <div class="url">www.korvelo.com</div><div class="pg">09</div>
</section>

<!-- 12 Question infographic -->
<section class="slide c4 r3">
  <div class="head-bar"></div><div class="head-title">Title Goes Here</div><div class="head-rule"></div><div class="head-logo">Korvelo</div>
  <div class="abs" role="img" aria-label="Question mark infographic built from orange and grey puzzle pieces" style="left:115px;top:42px;width:58px;height:88px;border-radius:30px 30px 8px 8px;background:linear-gradient(135deg,var(--orange),#b5b5b5 60%,var(--orange-light))"></div>
  <div class="abs" style="left:138px;top:134px;width:11px;height:11px;background:#111;border-radius:2px"></div>
  <div class="txt" style="left:28px;top:64px;width:68px;text-align:right">Why small firms face the same threats as large ones.</div>
  <div class="txt" style="left:28px;top:85px;width:68px;text-align:right">How quickly a breach can halt daily business.</div>
  <div class="txt" style="left:28px;top:106px;width:68px;text-align:right">What simple steps cut most common risks.</div>
  <div class="dot" style="left:100px;top:66px;width:2px;height:2px;background:var(--orange)"></div><div class="dot" style="left:100px;top:87px;width:2px;height:2px;background:#999"></div><div class="dot" style="left:100px;top:108px;width:2px;height:2px;background:#999"></div>
  <div class="dot" style="left:182px;top:66px;width:2px;height:2px;background:var(--orange)"></div><div class="dot" style="left:182px;top:87px;width:2px;height:2px;background:var(--orange)"></div><div class="dot" style="left:182px;top:108px;width:2px;height:2px;background:#999"></div>
  <div class="txt" style="left:190px;top:64px;width:68px">Who watches your systems after office hours.</div>
  <div class="txt" style="left:190px;top:85px;width:68px">Where your backups are kept and tested.</div>
  <div class="txt" style="left:190px;top:106px;width:68px">When your last security review took place.</div>
  <div class="url">www.korvelo.com</div><div class="pg">10</div>
</section>

<!-- 13 Team -->
<section class="slide c1 r4">
  <div class="head-bar"></div><div class="head-title">Title Goes Here</div><div class="head-rule"></div><div class="head-logo">Korvelo</div>
  <div class="abs" role="img" aria-label="Portrait of team member" style="left:59px;top:27px;width:34px;height:34px;border-radius:50%;background:radial-gradient(#e9e3de,#b9b2ad)"></div>
  <div class="abs" role="img" aria-label="Portrait of team member" style="left:139px;top:27px;width:34px;height:34px;border-radius:50%;background:radial-gradient(#d8c4b8,#6e4e45)"></div>
  <div class="abs" role="img" aria-label="Portrait of team member" style="left:219px;top:27px;width:34px;height:34px;border-radius:50%;background:radial-gradient(#f2efec,#c5bfba)"></div>
  <div class="abs" role="img" aria-label="Portrait of team member" style="left:59px;top:87px;width:34px;height:34px;border-radius:50%;background:radial-gradient(#e9e3de,#b9b2ad)"></div>
  <div class="abs" role="img" aria-label="Portrait of team member" style="left:139px;top:87px;width:34px;height:34px;border-radius:50%;background:radial-gradient(#d8c4b8,#6e4e45)"></div>
  <div class="abs" role="img" aria-label="Portrait of team member" style="left:219px;top:87px;width:34px;height:34px;border-radius:50%;background:radial-gradient(#f2efec,#c5bfba)"></div>
  <div class="member" style="left:56px;top:64px"><b>Team Member</b><br>Chief Executive<br>Officer</div>
  <div class="member" style="left:136px;top:64px"><b>Team Member</b><br>Chief Executive<br>Officer</div>
  <div class="member" style="left:216px;top:64px"><b>Team Member</b><br>Chief Executive<br>Officer</div>
  <div class="member" style="left:56px;top:124px"><b>Team Member</b><br>Chief Executive<br>Officer</div>
  <div class="member" style="left:136px;top:124px"><b>Team Member</b><br>Chief Executive<br>Officer</div>
  <div class="member" style="left:216px;top:124px"><b>Team Member</b><br>Chief Executive<br>Officer</div>
  <div class="url">www.korvelo.com</div><div class="pg">11</div>
</section>

<!-- 14 Stairs -->
<section class="slide c2 r4">
  <div class="head-bar"></div><div class="head-title">Title Goes Here</div><div class="head-rule"></div><div class="head-logo">Korvelo</div>
  <div class="dot" style="left:17px;top:33px;width:2.5px;height:2.5px;background:var(--orange)"></div><div class="txt" style="left:25px;top:32px;width:200px">Assess current defences and list every connected device.</div>
  <div class="dot" style="left:17px;top:46px;width:2.5px;height:2.5px;background:var(--orange-light)"></div><div class="txt" style="left:25px;top:45px;width:200px">Set priorities together and agree on a clear timeline.</div>
  <div class="dot" style="left:17px;top:59px;width:2.5px;height:2.5px;background:#aaa"></div><div class="txt" style="left:25px;top:58px;width:200px">Deploy protection tools and train the whole team.</div>
  <div class="dot" style="left:17px;top:72px;width:2.5px;height:2.5px;background:#111"></div><div class="txt" style="left:25px;top:71px;width:200px">Monitor, report and improve month after month.</div>
  <svg class="abs" style="left:110px;top:85px" width="165" height="70" viewBox="0 0 165 70">
    <polyline points="6,62 6,48 30,48" fill="none" stroke="var(--orange)" stroke-width="2.5"/><polygon points="30,45 35,48 30,51" fill="var(--orange)"/>
    <polyline points="44,46 44,32 68,32" fill="none" stroke="var(--orange-light)" stroke-width="2.5"/><polygon points="68,29 73,32 68,35" fill="var(--orange-light)"/>
    <polyline points="82,30 82,16 106,16" fill="none" stroke="#aaa" stroke-width="2.5"/><polygon points="106,13 111,16 106,19" fill="#aaa"/>
    <polyline points="118,14 118,4 150,4" fill="none" stroke="#111" stroke-width="2.5"/><polygon points="150,1 155,4 150,7" fill="#111"/>
    <circle cx="12" cy="36" r="3" fill="var(--orange)"/><circle cx="50" cy="20" r="3" fill="var(--orange-light)"/><circle cx="88" cy="5" r="3" fill="#aaa"/>
    <text x="12" y="57" font-size="3" fill="#333">Text</text><text x="50" y="41" font-size="3" fill="#333">Text</text><text x="88" y="25" font-size="3" fill="#333">Text</text><text x="124" y="12" font-size="3" fill="#333">Text</text>
  </svg>
  <div class="url">www.korvelo.com</div><div class="pg">12</div>
</section>

<!-- 15 Contact -->
<section class="slide c3 r4">
  <div class="abs" role="img" aria-label="Photo of a business handshake in orange tint" style="inset:0;background:linear-gradient(100deg,var(--orange) 0%,#f5a27c 35%,#fff 55%,#f7b08f 80%,var(--orange) 100%)"></div>
  <div class="abs" style="left:13px;top:8px;width:254px;height:142px;border:.8px solid rgba(255,255,255,.8)"></div>
  <div class="abs" style="left:17px;top:12px;font-size:5.6px;color:#222">Contact Information</div>
  <div class="abs" style="left:82px;top:103px;width:12px;height:12px;border-radius:50%;background:#f58a5a;border:1px solid #fff"></div>
  <div class="abs" style="left:134px;top:103px;width:12px;height:12px;border-radius:50%;background:#f58a5a;border:1px solid #fff"></div>
  <div class="abs" style="left:186px;top:103px;width:12px;height:12px;border-radius:50%;background:#f58a5a;border:1px solid #fff"></div>
  <div class="txt" style="left:68px;top:119px;width:40px;text-align:center;color:#333">Name</div>
  <div class="txt" style="left:120px;top:119px;width:40px;text-align:center;color:#333">+34 91 000 000</div>
  <div class="txt" style="left:172px;top:119px;width:40px;text-align:center;color:#333">hello@korvelo.com</div>
</section>

<!-- 16 Thank you light -->
<section class="slide c4 r4">
  <svg class="stripes" viewBox="0 0 280 158"><polygon points="256,0 268,0 238,50 226,50" fill="var(--orange)"/><polygon points="272,0 280,0 280,6 252,50 244,50" fill="var(--orange-light)"/><polygon points="216,134 228,134 214,158 202,158" fill="var(--orange)"/><polygon points="232,134 244,134 230,158 218,158" fill="var(--orange-light)"/></svg>
  <div class="title-big" style="left:24px;top:27px">THANK YOU!</div>
  <div class="subtitle" style="left:24px;top:42px">Your Subtitle Goes Here</div>
  <div class="txt" style="left:24px;top:50px;width:130px">Thank you for your time. Let us keep your business safe together.</div>
  <div class="brand" style="left:24px;top:103px">Korvelo</div>
  <div class="brand-tag" style="left:25px;top:120px">CYBERSECURITY</div>
  <div class="photo-circle" role="img" aria-label="Photo of a person facing a wall of technology icons" style="left:176px;top:44px;width:88px;height:88px;background:radial-gradient(circle,#5c7ea6,#1d3350)"></div>
</section>

<!-- 17 Thank you dark -->
<section class="slide c1 r5">
  <div class="abs" style="left:0;top:0;width:280px;height:115px;background:#000"></div>
  <svg class="stripes" viewBox="0 0 280 158"><polygon points="256,0 268,0 238,50 226,50" fill="var(--orange)"/><polygon points="272,0 280,0 280,6 252,50 244,50" fill="var(--orange-light)"/><polygon points="216,134 228,134 214,158 202,158" fill="var(--orange)"/><polygon points="232,134 244,134 230,158 218,158" fill="var(--orange-light)"/></svg>
  <div class="title-big" style="left:24px;top:27px">THANK YOU!</div>
  <div class="subtitle" style="left:24px;top:42px">Your Subtitle Goes Here</div>
  <div class="txt w" style="left:24px;top:50px;width:130px">Thank you for your time. Let us keep your business safe together.</div>
  <div class="brand" style="left:24px;top:127px">Korvelo</div>
  <div class="brand-tag" style="left:25px;top:143px">CYBERSECURITY</div>
  <div class="photo-circle" role="img" aria-label="Photo of hands using a calculator" style="left:172px;top:34px;width:92px;height:92px;background:radial-gradient(circle at 45% 45%,#fbf6f2,#b9a79a)"></div>
</section>

<!-- 18 Thank you chevron -->
<section class="slide c2 r5" style="background:#222">
  <svg class="stripes" viewBox="0 0 280 158">
    <defs><linearGradient id="chev" x1="0" y1="0" x2="1" y2="1"><stop offset="0" stop-color="var(--orange-light)"/><stop offset="1" stop-color="var(--orange)"/></linearGradient></defs>
    <polygon points="80,0 110,0 30,79 110,158 80,158 0,79" fill="url(#chev)"/>
    <polygon points="0,40 30,79 0,118" fill="#3a3a3a" opacity=".6"/>
    <polygon points="220,0 280,0 280,40" fill="#2c2c2c"/>
  </svg>
  <div class="abs" style="left:0;width:280px;top:70px;text-align:center;font-family:'Montserrat',sans-serif;font-weight:600;font-size:11px;color:#fff">THANK YOU !</div>
  <div class="txt w" style="left:85px;top:90px;width:110px;text-align:center">Thank you for your time. Let us keep your business safe together.</div>
  <div class="abs" style="left:120px;top:146px;display:flex;gap:2px">
    <span style="width:5px;height:5px;background:#4a7ab8"></span><span style="width:5px;height:5px;background:#4aa8d8"></span><span style="width:5px;height:5px;background:#777"></span><span style="width:5px;height:5px;background:#4aa8d8"></span><span style="width:5px;height:5px;background:#3a76b0"></span><span style="width:5px;height:5px;background:var(--orange-light)"></span>
  </div>
</section>

</body>
</html>
```